Carvo Group Business Card

Building Management company based in Sydney, Australia. We provide onsite management for commercial and residential buildings.
I would like a sophisticated minimalist design that indicates that we provide a high-end service. I would like a silver or metal look background or something similar.
The business card should have:
Name
Title
email
Office Phone
Mobile
Address
Website
The services that we provide should be prominent:
Building Management - Concierge - Caretaking - Cleaning

```html
<!DOCTYPE html>
<html lang="en">
<head>
<meta charset="utf-8">
<title>Carvo Group Business Card</title>
<link rel="stylesheet" href="https://fonts.googleapis.com/css2?family=Arimo:wght@400;700&display=swap">
<style>
  :root {
    --backdrop: #d9d9d9;
    --metal-light: #9a9a9a;
    --metal-mid: #5c5c5c;
    --metal-dark: #2b2b2b;
    --band-dark: #222222;
    --ink-black: #0d0d0d;
    --ink-blue: #3a7fc4;
    --ink-grey: #8a8a8a;
    --ink-emboss: #4a4a4a;
    --ink-light: #b4b4b4;
  }
  * { box-sizing: border-box; margin: 0; padding: 0; }
  html, body { width: 1200px; height: 900px; overflow: hidden; }
  body {
    background: var(--backdrop);
    font-family: "Arimo", Arial, sans-serif;
    display: flex;
    align-items: center;
    justify-content: center;
    gap: 60px;
  }
  .card {
    position: relative;
    width: 520px;
    height: 320px;
    border-radius: 14px;
    overflow: hidden;
    background: linear-gradient(180deg, var(--metal-dark) 0%, var(--metal-light) 38%, var(--metal-mid) 50%, var(--band-dark) 50.5%, var(--metal-dark) 100%);
    box-shadow: 0 12px 28px rgba(0,0,0,0.35);
  }
  .card::after {
    content: "";
    position: absolute;
    inset: 0;
    background: radial-gradient(ellipse at 50% 35%, rgba(255,255,255,0.22), rgba(255,255,255,0) 60%);
    pointer-events: none;
  }
  .card-front .brand {
    position: absolute;
    left: 0; right: 0; top: 118px;
    display: flex;
    align-items: center;
    justify-content: center;
    gap: 14px;
  }
  .brand-mark {
    width: 22px; height: 22px;
    background: var(--ink-black);
  }
  .brand-name {
    font-weight: 700;
    font-size: 46px;
    letter-spacing: 1px;
    color: var(--ink-black);
    text-transform: uppercase;
  }
  .website {
    position: absolute;
    top: 180px; left: 0; right: 0;
    text-align: center;
    font-size: 15px;
    color: var(--ink-light);
  }
  .person { position: absolute; top: 214px; left: 0; right: 0; text-align: center; }
  .person-name { font-size: 24px; color: #d0d0d0; }
  .person-name .first { color: var(--ink-blue); }
  .person-title { margin-top: 4px; font-size: 13px; letter-spacing: 5px; color: var(--ink-grey); }
  .services {
    position: absolute;
    top: 280px; left: 0; right: 0;
    text-align: center;
    font-size: 12px;
    letter-spacing: 1.5px;
    text-transform: uppercase;
    color: var(--ink-light);
  }
  .services .sep { margin: 0 6px; color: var(--ink-blue); }

  .card-back .brand-name-emboss {
    position: absolute;
    top: 150px; left: 0; right: 0;
    text-align: center;
    font-weight: 700;
    font-size: 40px;
    letter-spacing: 1px;
    color: var(--ink-emboss);
    text-transform: uppercase;
    text-shadow: 0 1px 0 rgba(255,255,255,0.12);
  }
  .phones {
    position: absolute;
    left: 34px; top: 222px;
    font-size: 17px;
    line-height: 30px;
    color: var(--ink-light);
  }
  .contact {
    position: absolute;
    right: 30px; top: 214px;
    font-size: 16px;
    color: var(--ink-light);
  }
  .contact-row { display: flex; align-items: flex-start; gap: 10px; margin-bottom: 10px; }
  .contact-row svg { flex: none; margin-top: 2px; }
  .address { font-size: 19px; line-height: 24px; }
</style>
</head>
<body>
  <section class="card card-front" aria-label="Business card front">
    <div class="brand">
      <span class="brand-mark"></span>
      <span class="brand-name">Carvo Group</span>
    </div>
    <p class="website">www.yourwebsitehere.com</p>
    <div class="person">
      <p class="person-name"><span class="first">Your</span> Name</p>
      <p class="person-title">Title</p>
    </div>
    <p class="services">Building Management<span class="sep">&bull;</span>Concierge<span class="sep">&bull;</span>Caretaking<span class="sep">&bull;</span>Cleaning</p>
  </section>

  <section class="card card-back" aria-label="Business card back">
    <p class="brand-name-emboss">Carvo Group</p>
    <div class="phones">
      <p>Tel 0123 456 789</p>
      <p>Mob 0123 456 789</p>
    </div>
    <div class="contact">
      <div class="contact-row">
        <svg width="22" height="18" viewBox="0 0 22 18" aria-hidden="true">
          <rect x="1" y="1" width="20" height="16" fill="none" stroke="#b4b4b4" stroke-width="1.6"/>
          <path d="M1 1 L11 10 L21 1" fill="none" stroke="#b4b4b4" stroke-width="1.6"/>
        </svg>
        <span>abcde@fghij.com</span>
      </div>
      <div class="contact-row">
        <svg width="22" height="22" viewBox="0 0 22 22" aria-hidden="true">
          <path d="M2 10 L11 2 L20 10" fill="none" stroke="#b4b4b4" stroke-width="1.6"/>
          <rect x="5" y="9" width="12" height="12" fill="none" stroke="#b4b4b4" stroke-width="1.6"/>
          <rect x="9" y="14" width="4" height="7" fill="#b4b4b4"/>
        </svg>
        <span class="address">Your Address<br>Goes Here</span>
      </div>
    </div>
  </section>
</body>
</html>
```